Need help refining Solkvartsgillet

Hi We need help with the refining of overall design and details of our homepage design Solkvartsgillet. See attached files.

Attached files:
homepage.psd - file you can use to work from.
homepage.png – quick notes on thoughts of the design
logo.psd (smart object) – The logo should be in gold.
social media elements.png - what type of data that needs design in the feed

What we need:
Something is missing with the overall design as well as detailed design for our social media feed. We don’t know what and hope you can solve this for us.

The homepage:
Our main page include a selfloading blogfeed combined with Pageloop- and Instagramfeed.

Fonts:
So far I´ve used Roboto regular, and Georgia, but feel free to use other fonts if you find better suited

Among others, we need a better detailed design that works better with the overall design.

Se attached sample image (social_mediafeed.png) what types of data we get from Pageloop in our feed. Feel free to redesign the elements of this data.

Headerlinks:
Even though we only have one page, there should be place for links to other pages as well which will load below the header.

Social media follow: Place for social media follow links/icons/buttons in style with rest of the design. Maybe at top grey border? We use Glimtora and Pageloop in style with rest of the design.

Colors:
The logo should be in gold, and use of "goldish" colors troughout the page.
Also blue elements troughout the page

Logo in gold/goldish color
Blue elements # 13416c (or similar color that works well in the design)

Target Market(s)

Wellness, fitness, spa and food, Exclusive

Number of Pages Required

1 page

Font styles to use
Serif
Sans Serif
Script
Other font styles liked:
• Roboto, Georgia

Requirements
Must have
• Better overall design that feel harmonic.
• Better design of blog and social media feeds (se all attached images)
• Nice clean design, easy on the eye
• Colors on theme: Gold + blue

```html
<!DOCTYPE html>
<html lang="sv">
<head>
<meta charset="utf-8">
<title>Solkvartsgillet</title>
<link rel="stylesheet" href="https://fonts.googleapis.com/css2?family=Gelasio:wght@400;700&family=Roboto:wght@400;500;700&display=swap">
<style>
:root{
  --navy:#13264a;
  --navy-deep:#0d1b36;
  --blue:#13416c;
  --gold:#d9ab3a;
  --gold-light:#f0cd6a;
  --gold-dark:#b8861f;
  --paper:#f3f2ef;
  --ink:#2b2b2b;
  --muted:#8a8a8a;
  --rule:#dcdad5;
  --white:#ffffff;
}
*{box-sizing:border-box;margin:0;padding:0}
html,body{width:1200px;height:2400px;overflow:hidden}
body{background:var(--paper);font-family:"Roboto",sans-serif;color:var(--ink);position:relative}

/* header */
.topbar{position:absolute;left:0;top:0;width:1200px;height:22px;background:var(--navy-deep)}
.mainnav{position:absolute;left:0;top:22px;width:1200px;height:90px;background:var(--navy);border-bottom:3px solid var(--gold)}
.mainnav ul{list-style:none;position:absolute;top:46px;display:flex;gap:26px;font-size:12px;line-height:16px;color:var(--white);text-transform:uppercase;letter-spacing:.5px;white-space:nowrap}
.nav-left{right:710px}
.nav-right{left:710px}
.mainnav li.active{color:var(--gold-light)}
.logo{position:absolute;left:520px;top:0;width:160px;height:112px;background:var(--navy);border:3px solid var(--gold);border-top:none;display:flex;flex-direction:column;align-items:center;justify-content:center;z-index:3}
.logo .mark{width:22px;height:22px;border-radius:50%;background:var(--gold);margin-bottom:10px}
.logo .name{font-family:"Gelasio",serif;font-size:17px;color:var(--gold)}
.social{position:absolute;right:270px;top:4px;display:flex;gap:8px;font-size:10px;line-height:14px;color:var(--gold-light)}
.dropdown{position:absolute;left:860px;top:115px;width:160px;background:var(--gold);z-index:4;border:1px solid var(--gold-dark)}
.dropdown div{padding:9px 14px;font-size:12px;color:var(--navy);border-bottom:1px solid var(--gold-light)}
.dropdown div:first-child{background:var(--gold-dark);color:var(--white)}
.dropdown div:last-child{border-bottom:none}

/* hero */
.hero{position:absolute;left:0;top:115px;width:1200px;height:330px;background:linear-gradient(100deg,#3c4a52 0%,#9fd4de 35%,#6fc3d2 60%,#2e3c44 100%)}
.hero-arrow{position:absolute;left:268px;top:255px;width:44px;height:44px;background:rgba(255,255,255,.2);border:1px solid rgba(255,255,255,.6)}
.hero-title{position:absolute;left:410px;top:222px;font-family:"Gelasio",serif;font-size:46px;line-height:56px;color:var(--white)}
.hero-sub{position:absolute;left:410px;top:284px;width:300px;font-size:12px;color:var(--white);background:rgba(19,38,74,.55);padding:8px 12px}
.hero-box{position:absolute;left:820px;top:262px;width:100px;height:40px;background:rgba(255,255,255,.85)}

/* offers */
.offers{position:absolute;left:0;top:445px;width:1200px;height:475px;background:linear-gradient(180deg,var(--gold-light),var(--gold) 45%,var(--gold-dark))}
.offers h2{position:absolute;left:0;top:42px;width:1200px;text-align:center;font-family:"Gelasio",serif;font-size:26px;color:var(--navy);font-weight:400}
.card{position:absolute;top:100px;width:220px;height:300px;background:var(--white);box-shadow:0 3px 10px rgba(0,0,0,.2)}
.card .pic{height:120px;background:linear-gradient(180deg,#8c6da8,#d98a7a 70%,#e9b16b);position:relative}
.card .pic span{position:absolute;left:12px;bottom:12px;font-family:"Gelasio",serif;font-size:30px;color:var(--white)}
.card .pic small{position:absolute;left:12px;top:10px;font-size:11px;color:var(--white)}
.card p{font-size:12px;color:var(--ink);padding:14px 14px 0;line-height:1.5}
.card .btn{position:absolute;left:14px;bottom:18px;width:60px;height:22px;background:var(--blue);color:var(--white);font-size:9px;text-align:center;line-height:22px;text-transform:uppercase}

/* article */
.article{position:absolute;left:260px;top:940px;width:680px}
.article h1{font-family:"Gelasio",serif;font-weight:400;font-size:30px;text-align:center;color:var(--navy)}
.meta{font-size:10px;color:var(--muted);text-align:center;margin-top:8px;letter-spacing:.4px}
.photo{margin-top:24px;height:320px;background:linear-gradient(110deg,#4b5960,#a8dbe3 45%,#7ac7d4 70%,#36444b)}
.body-text{margin-top:26px;font-size:12px;line-height:1.8;color:#444}
.dropcap{float:left;font-family:"Gelasio",serif;font-size:50px;line-height:44px;margin:4px 8px 0 0;color:var(--navy)}
.article h3{font-family:"Gelasio",serif;font-size:20px;font-weight:400;margin:22px 0 10px;color:var(--navy)}
.readmore{text-align:right;font-size:10px;margin-top:18px;text-transform:uppercase;color:var(--blue)}
.share{margin-top:14px;display:flex;gap:8px;align-items:center;font-size:10px;color:var(--muted);border-bottom:1px solid var(--rule);padding-bottom:14px}
.share i{width:14px;height:14px;border-radius:50%;background:var(--blue);display:inline-block}
.share i.g{background:var(--gold)}

/* feed */
.feed{position:absolute;left:260px;width:680px;height:300px;border-bottom:1px solid var(--rule)}
.feed .txt{position:absolute;left:0;top:10px;width:320px;font-size:11px;line-height:1.7;color:#444}
.feed .src{font-size:10px;font-weight:700;text-transform:uppercase;color:var(--navy)}
.feed .date{font-size:9px;color:var(--muted);margin-bottom:16px}
.feed .lead{font-size:12px;line-height:1.7;margin-bottom:10px}
.feed .lead b{font-family:"Gelasio",serif;font-size:22px;line-height:20px;color:var(--navy);font-weight:400}
.feed .img{position:absolute;right:0;top:10px;width:320px;height:280px}
.feed.one{top:1660px}
.feed.two{top:1990px}
.room{background:linear-gradient(180deg,#6e4a33,#b88f6c 45%,#e8e2d8 75%,#cfc6b8)}
.drinks{background:linear-gradient(180deg,#c9d3da,#6a7f8e 40%,#d79a3a 70%,#eadfce)}
</style>
</head>
<body>
<header>
  <div class="topbar"></div>
  <div class="social"><span>Pageloop</span><span>Glimtora</span></div>
  <nav class="mainnav">
    <ul class="nav-left"><li>Hem</li><li>Solkvartsgillet</li><li class="active">Erbjudanden</li></ul>
    <ul class="nav-right"><li>Medlemserbjudanden</li><li>Om</li><li>Kontakt</li></ul>
  </nav>
  <div class="logo"><span class="mark"></span><span class="name">Solkvartsgillet</span></div>
  <div class="dropdown"><div>Kontakt</div><div>Om klubben</div><div>Villkor</div></div>
</header>

<section class="hero" role="img" aria-label="Kvinna som kopplar av i en blå lagun bland lavastenar"></section>
<div class="hero-arrow"></div>
<div class="hero-title">Featured</div>
<div class="hero-sub">Koppla av i varma källor med utsikt över lavan</div>
<div class="hero-box"></div>

<section class="offers">
  <h2>Solkvartsgillets Medlemserbjudanden</h2>
  <div class="card" style="left:260px"><div class="pic" role="img" aria-label="Solnedgång över hav"><small>Spara 30% på spa</small><span>30%</span></div><p>Spara 30% på ditt spabesök<br>Gäller alla medlemmar</p><div class="btn">Läs mer</div></div>
  <div class="card" style="left:490px"><div class="pic" role="img" aria-label="Solnedgång över hav"><small>Spara 30% på spa</small><span>30%</span></div><p>Spara 30% på ditt spabesök<br>Gäller alla medlemmar</p><div class="btn">Läs mer</div></div>
  <div class="card" style="left:720px"><div class="pic" role="img" aria-label="Solnedgång över hav"><small>Spara 30% på spa</small><span>30%</span></div><p>Spara 30% på ditt spabesök<br>Gäller alla medlemmar</p><div class="btn">Läs mer</div></div>
</section>

<article class="article">
  <h1>En trevlig rubrik på ditt blogginlägg</h1>
  <p class="meta">PUBLICERAT 12 MAJ AV REDAKTIONEN I KATEGORIN SPA · 3 KOMMENTARER</p>
  <div class="photo" role="img" aria-label="Kvinna i blå lagun med mörka stenar"></div>
  <p class="body-text"><span class="dropcap">E</span>n lugn morgon i de varma källorna ger kropp och själ ny kraft. Vi besökte lagunen tidigt, innan resten av gästerna vaknat, och fick hela vattnet för oss själva. Här delar vi med oss av våra bästa tips för en avkopplande helg med god mat, mjuka handdukar och tid för vila. Missa inte kvällsbadet när himlen skiftar i guld och blått över lavafälten runt omkring.</p>
  <h3>Rubrik 2</h3>
  <p class="body-text" style="margin-top:0">Efter badet väntade en lätt lunch med lokala råvaror och färska örter. Restaurangen ligger bara några steg från lagunen och erbjuder både vegetariska rätter och fisk från trakten. Boka gärna bord i förväg under högsäsong och fråga efter fönsterplatserna mot vattnet.</p>
  <p class="readmore">Läs mer ›</p>
  <div class="share"><i></i><i class="g"></i><i></i><span>Dela · 3 kommentarer</span></div>
</article>

<section class="feed one">
  <div class="txt">
    <div class="src">Glimtora</div>
    <div class="date">3 timmar sedan · 24 gillar</div>
    <p class="lead"><b>N</b>u kan du checka in i våra nyrenoverade rum med utsikt över trädgården och spaavdelningen.</p>
    <p>Mjuka sängar, ljusa färger och frukost på rummet ingår för alla medlemmar denna månad.</p>
  </div>
  <div class="img room" role="img" aria-label="Hotellrum med bäddad säng och lampor"></div>
</section>

<section class="feed two">
  <div class="txt">
    <div class="src">Pageloop</div>
    <div class="date">I går · 41 gillar</div>
    <p class="lead"><b>S</b>val dryck vid vattnet</p>
    <p>Avsluta dagen med en kall dryck på terrassen. Våra bartenders blandar säsongens favoriter med färsk citrus och örter från köksträdgården. Terrassen är öppen alla dagar fram till sen kväll.</p>
  </div>
  <div class="img drinks" role="img" aria-label="Två glas med kall dryck framför en sjö"></div>
</section>
</body>
</html>
```